Webpage for balustrade importer and installer

We are a balustrade importer and installer. We sell a few different products mostly connected with glass and aluminum. We sell balconies, stairs, shower glass, mirrors, splash back glass, office partitions, glass dors and walls.

```html
<!DOCTYPE html>
<html lang="en">
<head>
<meta charset="utf-8">
<title>NORDRAIL – Balustrade Importer &amp; Installer</title>
<link rel="stylesheet" href="https://fonts.googleapis.com/css2?family=Roboto+Condensed:wght@300;400;700&family=Roboto:ital,wght@0,400;0,500;0,700;1,400&display=swap">
<style>
:root{
  --blue:#3352a8;
  --blue-deep:#2d4aa0;
  --blue-soft:rgba(66,95,185,.93);
  --orange:#f0900f;
  --ink:#222631;
  --text:#7d8088;
  --line:#e6e8ee;
  --white:#fff;
}
*{box-sizing:border-box;margin:0;padding:0}
html,body{width:1200px;height:3939px;overflow:hidden;background:var(--white)}
body{position:relative;font-family:"Roboto",Arial,sans-serif;color:var(--ink)}
.abs{position:absolute}
.center{text-align:center}
.cond{font-family:"Roboto Condensed","Arial Narrow",sans-serif}

/* hero */
.hero{left:0;top:0;width:1200px;height:616px;background:linear-gradient(180deg,#2c3f63 0%,#3a5279 45%,#6d7f9c 70%,#8c97a8 100%)}
.header-rule{left:0;top:99px;width:1200px;height:1px;background:rgba(255,255,255,.35)}
.logo{font-family:"Roboto Condensed",sans-serif;font-weight:300;color:var(--white);font-size:38px;letter-spacing:-.5px;line-height:1}
.nav a{position:absolute;top:44px;color:var(--white);font-size:14px;text-decoration:none}
.nav-active{left:390px;top:95px;width:62px;height:4px;background:var(--white)}
.call-circle{left:870px;top:23px;width:46px;height:46px;border-radius:50%;background:var(--white)}
.call-label{left:927px;top:25px;color:var(--white);font-size:13px}
.call-number{left:927px;top:44px;color:var(--white);font-size:22px;font-weight:700}
.hero-title{left:0;top:258px;width:1200px;color:var(--white);font-size:42px;font-weight:700;letter-spacing:.5px}
.hero-text{left:220px;top:317px;width:760px;color:var(--white);font-size:14px;line-height:26px}
.btn{display:flex;align-items:center;justify-content:center;color:var(--white);font-size:14px;font-weight:700;border-radius:3px}
.btn-start{left:529px;top:385px;width:141px;height:48px;background:var(--blue)}
.dots{left:573px;top:533px;display:flex;gap:8px}
.dots span{width:11px;height:11px;border-radius:50%;background:var(--white)}

/* utility bar */
.util{left:0;top:616px;width:1200px;height:95px;background:var(--blue)}
.util-item{position:absolute;top:40px;color:var(--white);font-size:13px;font-weight:700;display:flex;align-items:center;gap:7px}

/* section headings */
.sec-rule{width:46px;height:3px;background:var(--ink)}
.sec-title{left:0;width:1200px;font-size:35px;font-weight:700;color:var(--ink)}
.sec-title .light{font-weight:300}

/* features */
.feature{width:300px;text-align:center}
.feature h3{font-size:21px;font-weight:500;margin-top:0;color:var(--ink)}
.feature p{font-size:14px;line-height:26px;color:var(--text);margin-top:10px}
.feature .go{margin-top:10px;display:block}

/* contact band */
.photo-band{left:0;top:1209px;width:1200px;height:407px;background:linear-gradient(180deg,#8fa7bf 0%,#b2bfc9 40%,#c7a088 68%,#9aa7a9 100%)}
.dot-field{left:40px;top:1636px;width:1120px;height:148px;background:#f3f5fa}
.contact-box{left:86px;top:1495px;width:1029px;height:245px;background:var(--blue-soft)}
.contact-title{left:0;top:34px;width:1029px;color:var(--white);font-size:35px;font-weight:700}
.contact-title .light{font-weight:300}
.field{position:absolute;top:92px;width:216px;height:51px;background:var(--white);color:#a4a7ae;font-size:13px;padding:18px 20px}
.btn-touch{left:432px;top:162px;width:164px;height:51px;background:var(--orange);font-size:14px}

/* products */
.prod-img{background:linear-gradient(135deg,#f4f5f7,#d5d8dd);border:1px solid #cfd2d7}
.chev{position:absolute;top:2118px}

/* testimonials */
.testi-photo{left:0;top:2442px;width:599px;height:399px;background:linear-gradient(160deg,#3e5f96 0%,#7d8ea8 35%,#c8ccd2 60%,#4c5562 100%)}
.card{position:absolute;top:2578px;height:206px;background:var(--white);box-shadow:0 4px 18px rgba(0,0,0,.12);text-align:center;padding:20px 32px}
.card p{font-size:13px;font-style:italic;line-height:26px;color:var(--text);margin-top:6px;text-align:justify;text-align-last:center}
.card .who{font-size:14px;font-weight:500;color:#444;margin-top:10px}

/* gallery */
.skyline{left:0;top:3420px;width:1200px;height:173px;background:linear-gradient(180deg,rgba(230,233,240,0),#e9ecf2)}
.dot-corner{left:958px;top:2927px;width:186px;height:268px;background:#f4f6fa}
.tile{position:absolute;width:310px;height:218px}
.zoom{position:absolute;inset:0;background:rgba(20,24,34,.35);border:3px solid #fff;box-shadow:0 0 0 1px #cfd2d7;display:flex;align-items:center;justify-content:center}

/* footer */
.footer{left:0;top:3593px;width:1200px;height:346px;background:var(--blue-deep)}
.foot-links{left:0;top:143px;width:1200px;color:var(--white);font-size:13px}
.foot-links span{margin:0 17px}
.foot-copy{left:0;top:181px;width:1200px;color:var(--white);font-size:13px}
.foot-legal{left:0;top:214px;width:1200px;color:var(--white);font-size:13px}
.foot-legal span{margin:0 17px}
</style>
</head>
<body>

<!-- Hero -->
<div class="abs hero" role="img" aria-label="Photo of a snowy wooden terrace with a frameless glass balustrade overlooking a town at dusk"></div>
<div class="abs header-rule"></div>
<div class="abs logo" style="left:110px;top:32px">NORDRAIL</div>
<nav class="nav">
  <a style="left:400px">Home</a>
  <a style="left:482px">About us</a>
  <a style="left:580px">Why us?</a>
  <a style="left:675px">Blog</a>
  <a style="left:746px">Contact us</a>
</nav>
<div class="abs nav-active"></div>
<div class="abs call-circle">
  <svg width="46" height="46" viewBox="0 0 46 46"><path d="M19 17c1-1 2 0 3 2s0 2-1 3c1 2 2 3 4 4 1-1 1-2 3-1s3 2 2 3c-1 2-3 3-6 1s-6-5-7-8c0-2 1-3 2-4z" fill="#3352a8"/></svg>
</div>
<div class="abs call-label">Call us Today :</div>
<div class="abs call-number">+1 555 014 2290</div>

<h1 class="abs hero-title cond center">BALUSTRADE IMPORTER &amp; INSTALLER</h1>
<p class="abs hero-text center">Lorem ipsum dolor sit amet, consectetur adipiscing elit, sed do eiusmod tempor incididunt ut labore et dolore magna aliqua. Ut enim ad minim veniam, quis nostrud</p>
<div class="abs btn btn-start">GET STARTED</div>
<div class="abs dots"><span></span><span></span><span></span></div>

<!-- Utility bar -->
<div class="abs util">
  <div class="util-item" style="left:321px">
    <svg width="13" height="13" viewBox="0 0 14 14"><circle cx="7" cy="7" r="6.5" fill="#fff"/><path d="M4 4c2 0 2 2 1 3s0 3 2 3M9 3c0 2 2 2 3 3" stroke="#3352a8" stroke-width="1.5" fill="none"/></svg>
    ENG
    <svg width="9" height="6" viewBox="0 0 9 6"><path d="M0 0h9L4.5 6z" fill="#fff"/></svg>
  </div>
  <div class="util-item" style="left:463px">
    <svg width="10" height="14" viewBox="0 0 10 14"><path d="M5 0a5 5 0 0 1 5 5c0 4-5 9-5 9S0 9 0 5a5 5 0 0 1 5-5z" fill="#fff"/><circle cx="5" cy="5" r="2" fill="#3352a8"/></svg>
    LOCATIONS
  </div>
  <div class="util-item" style="left:625px">
    <svg width="13" height="13" viewBox="0 0 14 14"><circle cx="7" cy="7" r="7" fill="#fff"/><path d="M4 7l2 2 4-4" stroke="#3352a8" stroke-width="2" fill="none"/></svg>
    PAYMENT
  </div>
  <div class="util-item" style="left:772px">
    <svg width="15" height="13" viewBox="0 0 15 13"><path d="M0 1h3l2 7h8l2-6H4" stroke="#fff" stroke-width="1.6" fill="none"/><circle cx="6" cy="11" r="1.5" fill="#fff"/><circle cx="12" cy="11" r="1.5" fill="#fff"/></svg>
    CART : $0.00
  </div>
</div>

<!-- Why choose -->
<div class="abs sec-rule" style="left:577px;top:789px"></div>
<h2 class="abs sec-title cond center" style="top:805px">WHY CHOOSE <span class="light">NORDRAIL?</span></h2>

<div class="abs feature" style="left:124px;top:886px">
  <svg width="70" height="70" viewBox="0 0 70 70"><rect x="14" y="2" width="26" height="64" fill="none" stroke="#c8a979" stroke-width="2"/><rect x="30" y="24" width="26" height="42" fill="none" stroke="#3352a8" stroke-width="2"/><g fill="none" stroke="#3352a8" stroke-width="2"><rect x="19" y="9" width="6" height="6"/><rect x="29" y="9" width="6" height="6"/><rect x="19" y="20" width="6" height="6"/><rect x="19" y="31" width="6" height="6"/><rect x="36" y="31" width="6" height="6"/><rect x="45" y="31" width="6" height="6"/><rect x="36" y="43" width="6" height="6"/><rect x="45" y="43" width="6" height="6"/><rect x="36" y="55" width="6" height="6"/><rect x="45" y="55" width="6" height="6"/></g><line x1="6" y1="67" x2="64" y2="67" stroke="#c8a979" stroke-width="2"/></svg>
  <h3>Lorem ipsum dolor</h3>
  <p>Lorem ipsum dolor sit amet, consectetur adipiscing elit, sed do eiusmod tempor incididunt ut labore</p>
  <svg class="go" style="margin:10px auto 0" width="22" height="10" viewBox="0 0 22 10"><path d="M0 5h19M15 1l5 4-5 4" stroke="#3352a8" stroke-width="2.2" fill="none"/></svg>
</div>
<div class="abs feature" style="left:450px;top:886px">
  <svg width="70" height="70" viewBox="0 0 70 70"><path d="M20 12a27 27 0 1 0 30 0" fill="none" stroke="#c8a979" stroke-width="2"/><path d="M26 32h-6v18h6zM26 34c6-2 8-8 10-14 3 0 4 3 3 8h11c3 0 3 4 1 5 2 1 2 4 0 5 2 1 1 4-1 5 1 2 0 4-3 4H26" fill="none" stroke="#3352a8" stroke-width="2"/></svg>
  <h3>Lorem ipsum dolor</h3>
  <p>Lorem ipsum dolor sit amet, consectetur adipiscing elit, sed do eiusmod tempor incididunt ut labore</p>
  <svg class="go" style="margin:10px auto 0" width="22" height="10" viewBox="0 0 22 10"><path d="M0 5h19M15 1l5 4-5 4" stroke="#3352a8" stroke-width="2.2" fill="none"/></svg>
</div>
<div class="abs feature" style="left:775px;top:886px">
  <svg width="70" height="70" viewBox="0 0 70 70"><circle cx="35" cy="27" r="20" fill="none" stroke="#c8a979" stroke-width="2"/><circle cx="35" cy="27" r="14" fill="none" stroke="#3352a8" stroke-width="2"/><path d="M35 18l3 6 6 1-4 4 1 6-6-3-6 3 1-6-4-4 6-1z" fill="none" stroke="#3352a8" stroke-width="2"/><path d="M24 44l-6 20 7-4 4 7 5-17M46 44l6 20-7-4-4 7-5-17" fill="none" stroke="#c8a979" stroke-width="2"/></svg>
  <h3>Lorem ipsum dolor</h3>
  <p>Lorem ipsum dolor sit amet, consectetur adipiscing elit, sed do eiusmod tempor incididunt ut labore</p>
  <svg class="go" style="margin:10px auto 0" width="22" height="10" viewBox="0 0 22 10"><path d="M0 5h19M15 1l5 4-5 4" stroke="#3352a8" stroke-width="2.2" fill="none"/></svg>
</div>

<!-- Same day contact -->
<div class="abs photo-band" role="img" aria-label="Photo of a woman leaning on a steel railing looking over a hillside town"></div>
<div class="abs dot-field" role="img" aria-label="Soft dotted backdrop"></div>
<div class="abs contact-box">
  <h2 class="abs contact-title cond center">SAME DAY <span class="light">CONTACT</span></h2>
  <div class="field" style="left:58px">First name</div>
  <div class="field" style="left:290px">Last name</div>
  <div class="field" style="left:522px">+x xxx xxx xxxx</div>
  <div class="field" style="left:755px">info@xxxx.com</div>
  <div class="abs btn btn-touch">GET IN TOUCH</div>
</div>

<!-- Products -->
<div class="abs sec-rule" style="left:577px;top:1843px"></div>
<h2 class="abs sec-title cond center" style="top:1859px">OUR PRODUCT</h2>

<svg class="chev" style="left:48px" width="18" height="30" viewBox="0 0 18 30"><path d="M15 2L3 15l12 13" stroke="#333" stroke-width="2.5" fill="none"/></svg>
<svg class="chev" style="left:1124px" width="18" height="30" viewBox="0 0 18 30"><path d="M3 2l12 13L3 28" stroke="#333" stroke-width="2.5" fill="none"/></svg>

<div class="abs prod-img" style="left:180px;top:1956px;width:86px;height:160px" role="img" aria-label="Aluminium balustrade post, front view"></div>
<div class="abs prod-img" style="left:282px;top:1956px;width:86px;height:160px" role="img" aria-label="Aluminium balustrade post with glass clamp"></div>

<div class="abs feature" style="left:450px;top:1962px">
  <h3>Lorem ipsum dolor</h3>
  <p>Lorem ipsum dolor sit amet, consectetur adipiscing elit, sed do eiusmod tempor incididunt ut labore</p>
  <svg class="go" style="margin:10px auto 0" width="22" height="10" viewBox="0 0 22 10"><path d="M0 5h19M15 1l5 4-5 4" stroke="#3352a8" stroke-width="2.2" fill="none"/></svg>
</div>

<div class="abs prod-img" style="left:832px;top:1962px;width:84px;height:159px" role="img" aria-label="Stainless handrail post with glass clamps"></div>
<div class="abs prod-img" style="left:931px;top:1962px;width:84px;height:159px" role="img" aria-label="Stainless handrail post with mounted glass panel"></div>

<div class="abs feature" style="left:124px;top:2168px">
  <h3>Lorem ipsum dolor</h3>
  <p>Lorem ipsum dolor sit amet, consectetur adipiscing elit, sed do eiusmod tempor incididunt ut labore</p>
  <svg class="go" style="margin:10px auto 0" width="22" height="10" viewBox="0 0 22 10"><path d="M0 5h19M15 1l5 4-5 4" stroke="#3352a8" stroke-width="2.2" fill="none"/></svg>
</div>

<div class="abs prod-img" style="left:515px;top:2157px;width:80px;height:150px" role="img" aria-label="Round stainless railing post with bar infill"></div>
<div class="abs prod-img" style="left:607px;top:2157px;width:80px;height:150px" role="img" aria-label="Round stainless railing post with glass infill"></div>

<div class="abs feature" style="left:775px;top:2168px">
  <h3>Lorem ipsum dolor</h3>
  <p>Lorem ipsum dolor sit amet, consectetur adipiscing elit, sed do eiusmod tempor incididunt ut labore</p>
  <svg class="go" style="margin:10px auto 0" width="22" height="10" viewBox="0 0 22 10"><path d="M0 5h19M15 1l5 4-5 4" stroke="#3352a8" stroke-width="2.2" fill="none"/></svg>
</div>

<!-- Testimonials -->
<div class="abs testi-photo" role="img" aria-label="Photo of a modern apartment block with glass balconies"></div>
<svg class="abs" style="left:1018px;top:2528px" width="70" height="14" viewBox="0 0 70 14"><path d="M22 7H2M7 2L2 7l5 5" stroke="#9aa0ab" stroke-width="1.5" fill="none"/><path d="M46 7h22M63 2l5 5-5 5" stroke="#f0900f" stroke-width="2" fill="none"/></svg>

<div class="card" style="left:437px;width:361px">
  <svg width="34" height="26" viewBox="0 0 34 26"><path d="M0 26V14C0 6 4 1 12 0v5c-4 1-6 4-6 8h6v13zM20 26V14c0-8 4-13 12-14v5c-4 1-6 4-6 8h6v13z" fill="#d7dae0"/></svg>
  <p>“Lorem ipsum dolor sit amet, consectetur adipisc ing elit, sed do eiusmod tempor incididunt ut labore et dolore magna aliqua. Ut enim ad minim veniam, quis nostrud exercitation”</p>
  <div class="who">- John Doe</div>
</div>
<div class="card" style="left:838px;width:362px">
  <svg width="34" height="26" viewBox="0 0 34 26"><path d="M0 26V14C0 6 4 1 12 0v5c-4 1-6 4-6 8h6v13zM20 26V14c0-8 4-13 12-14v5c-4 1-6 4-6 8h6v13z" fill="#d7dae0"/></svg>
  <p>“Lorem ipsum dolor sit amet, consectetur adipisc ing elit, sed do eiusmod tempor incididunt ut labore et dolore magna aliqua. Ut enim ad minim veniam, quis nostrud exercitation”</p>
  <div class="who">- John Doe</div>
</div>

<!-- Gallery -->
<div class="abs dot-corner" role="img" aria-label="Soft dotted corner backdrop"></div>
<div class="abs skyline" role="img" aria-label="Faint city skyline backdrop"></div>
<div class="abs sec-rule" style="left:577px;top:2942px"></div>
<h2 class="abs sec-title cond center" style="top:2958px">GALLERY</h2>

<div class="tile" style="left:112px;top:3032px;background:linear-gradient(135deg,#e7e2dc,#b98e62 55%,#5d4a3c)" role="img" aria-label="Staircase with glass balustrade and warm lamp light"></div>
<div class="tile" style="left:445px;top:3032px;background:linear-gradient(180deg,#4a4d55,#2c2e33 60%,#5a5c62)" role="img" aria-label="Dark timber house with balcony railing">
  <div class="zoom"><svg width="26" height="26" viewBox="0 0 26 26"><circle cx="11" cy="11" r="8" fill="none" stroke="#fff" stroke-width="2.5"/><path d="M17 17l7 7M11 7v8M7 11h8" stroke="#fff" stroke-width="2.5"/></svg></div>
</div>
<div class="tile" style="left:777px;top:3032px;background:linear-gradient(160deg,#dcdcdc,#8b8f93 50%,#6d5a4a)" role="img" aria-label="Interior stair with steel and glass railing"></div>
<div class="tile" style="left:112px;top:3273px;background:linear-gradient(135deg,#f2f2f0,#dcd6cc 50%,#c47c3e)" role="img" aria-label="Floating timber stair with glass balustrade"></div>
<div class="tile" style="left:445px;top:3273px;background:linear-gradient(180deg,#a8b4c2,#8d9aa8 55%,#c5c3bf)" role="img" aria-label="Balcony glass railing facing the sea"></div>
<div class="tile" style="left:777px;top:3273px;background:linear-gradient(180deg,#8a7a52,#6c7480 45%,#9a9ca0)" role="img" aria-label="Roof terrace with glass balustrade"></div>

<!-- Footer -->
<footer class="abs footer">
  <div class="abs logo center" style="left:0;width:1200px;top:80px">NORDRAIL</div>
  <div class="abs foot-links center">HOME<span>|</span>ABOUT US<span>|</span>WHY US?<span>|</span>BLOG<span>|</span>CONTACT US</div>
  <div class="abs foot-copy center">© Copyrights 2020 NORDRAIL | All Rights Reserved</div>
  <div class="abs foot-legal center">Terms &amp; Condition<span>|</span>Privacy policy<span>|</span>Disclaimer</div>
</footer>

</body>
</html>
```